Tallow Crest Business Card

We need a business card designed for a a company called "Tallow Crest". We offer consulting, coaching and training to business leaders and coaches (across the world) using the latest findings in neuroscience, social and emotional intelligence and positive psychology. The final design should communicate the use of brain science to create sustainable relationships.

The card should be doublesided. The logo is attached and names and titles will be provided to the successful designer. Thank you.

Industry/Entity Type

Training

```html
<!DOCTYPE html>
<html lang="en">
<head>
<meta charset="utf-8">
<title>Tallow Crest Business Card</title>
<link rel="stylesheet" href="https://fonts.googleapis.com/css2?family=Open+Sans:wght@400;600;800&display=swap">
<style>
  :root {
    --page: #e9e6e1;
    --card-white: #ffffff;
    --card-black: #0c0c0c;
    --brand-blue: #0a86c4;
    --brand-green: #b4d60f;
    --ink: #161616;
    --rule: #9a9a9a;
    --on-dark: #f2f2f2;
  }
  * { box-sizing: border-box; margin: 0; padding: 0; }
  html, body { width: 1200px; height: 900px; overflow: hidden; }
  body {
    background: var(--page);
    font-family: "Open Sans", Arial, sans-serif;
    display: flex;
    align-items: center;
    justify-content: center;
    gap: 40px;
  }
  .card {
    position: relative;
    width: 540px;
    height: 350px;
    overflow: hidden;
    box-shadow: 0 6px 18px rgba(0,0,0,0.18);
  }
  .wordmark {
    font-family: "Open Sans", Arial, sans-serif;
    font-weight: 800;
    color: var(--brand-blue);
    letter-spacing: 0.5px;
    display: flex;
    align-items: center;
    gap: 10px;
    white-space: nowrap;
  }
  .wordmark-dot {
    width: 14px; height: 14px;
    border-radius: 50%;
    background: var(--brand-green);
  }

  /* Back side */
  .card-back { background: var(--card-black); }
  .card-back .wordmark {
    position: absolute;
    left: 0; right: 0; top: 128px;
    justify-content: center;
    font-size: 40px;
  }
  .card-back .web {
    position: absolute;
    left: 0; right: 0; top: 208px;
    text-align: center;
    color: var(--on-dark);
    font-size: 15px;
    letter-spacing: 0.3px;
  }

  /* Front side */
  .card-front { background: var(--card-white); }
  .card-front .wordmark {
    position: absolute;
    left: 30px; top: 56px;
    font-size: 30px;
  }
  .person {
    position: absolute;
    left: 30px; top: 150px;
    color: var(--ink);
  }
  .person-name { font-size: 24px; font-weight: 400; line-height: 1.1; }
  .person-title { font-size: 15px; line-height: 1.4; }
  .contact {
    position: absolute;
    left: 262px; top: 120px;
    padding-left: 14px;
    border-left: 1px solid var(--rule);
    list-style: none;
    color: var(--ink);
    font-size: 13.5px;
    line-height: 20px;
  }
  .contact li { display: flex; align-items: center; gap: 8px; white-space: nowrap; }
  .contact svg { width: 12px; height: 12px; flex: none; fill: var(--brand-blue); }
  .swoosh { position: absolute; left: 0; bottom: 0; width: 540px; height: 350px; }
</style>
</head>
<body>

<section class="card card-back" aria-label="Back of card">
  <div class="wordmark"><span class="wordmark-dot"></span>Tallow Crest</div>
  <p class="web">www.tallowcrest.de</p>
</section>

<section class="card card-front" aria-label="Front of card">
  <svg class="swoosh" viewBox="0 0 540 350" aria-hidden="true">
    <path d="M0,246 C170,248 330,292 540,312 L540,350 L0,350 Z" fill="var(--brand-green)"/>
    <path d="M0,258 C170,262 330,302 540,322 L540,350 L0,350 Z" fill="var(--brand-blue)"/>
  </svg>

  <div class="wordmark"><span class="wordmark-dot"></span>Tallow Crest</div>

  <div class="person">
    <p class="person-name">Corin Vessel</p>
    <p class="person-title">Director</p>
  </div>

  <ul class="contact">
    <li><svg viewBox="0 0 12 12"><path d="M6 1 L11 6 H9.5 V11 H7 V8 H5 V11 H2.5 V6 H1 Z"/></svg>Lindenweg 18, 40213 Düsseldorf</li>
    <li><svg viewBox="0 0 12 12"><path d="M1 3 H11 V10 H1 Z M1.8 3.6 L6 7 L10.2 3.6" fill="none" stroke="var(--brand-blue)" stroke-width="1"/></svg>info@tallowcrest.de</li>
    <li><svg viewBox="0 0 12 12"><circle cx="6" cy="6" r="5"/><path d="M1 6 H11 M6 1 V11 M2.5 3.5 H9.5 M2.5 8.5 H9.5" stroke="#fff" stroke-width="0.7" fill="none"/></svg>www.tallowcrest.de</li>
    <li><svg viewBox="0 0 12 12"><path d="M1 4 Q6 0 11 4 L9.5 5.5 L8 4.5 V3.5 H4 V4.5 L2.5 5.5 Z M3 6 H9 L10 11 H2 Z"/></svg>0211 / 55 40 12 30</li>
    <li><svg viewBox="0 0 12 12"><path d="M3 1 H8 V4 H3 Z M1 5 H11 V11 H1 Z"/></svg>0211 / 55 40 12 39</li>
    <li><svg viewBox="0 0 12 12"><path d="M3 0.5 H9 V11.5 H3 Z M4 2 V9 H8 V2 Z"/></svg>0151 / 204 88 316</li>
  </ul>
</section>

</body>
</html>
```